Australian Online Training Organisation needs a Website Design

We need a Web Design ideally using a Wordpress Divi template which will represent an Australian Online Training Company.

(Harlow Net Learning)

The website will represent a range of short courses with an emphasis on business, zentrosoft, leadership etc.

The website will 'shell out' to the third party portal where 'bookings' occur. I am imaging a fantastic looking web design with perhaps 5-6 pages.

I am wondering if a selection of courses including the below list can be incorporated?

The variety of courses include :

Workplace Safety
Sales Training
Leadership
Process Management
Problem Solving
Project Management
Business Planning
Meetings and Events
Emotional Intelligence
Human Resources
Administrative Essentials
Customer Service
Career Development
Conflict Resolution
Train the Trainer
Supervisors and Managers
Internet marketing
Communications
Team Building
Marketing
Finance
Writing
Job Search Skills
Public Speaking
Negotiation Skills
Talent Management
Zentrosoft Deskline 2016
ZDC Preparation for Office 2010
Office 2013
Office 2010
Upgrading to Office 2010
Computer Fundamentals
Upgrading to Office 2007
Office 2003
Office 2002
Pavra Suite X3
Core Essentials
Office 2007

Thank you so much for all of the amazing designs we received. We were so happy with so many elements that it was very hard to choose. Our top two were very hard to decide upon but we look forward to working more with both of these talents into the future. Thank you again.

Target Market(s)

Professionals, students and workers who would like to improve their skills with online training in over 500 + courses -

Industry/Entity Type

It Company

Number of Pages Required

5+ page

Font styles to use
Sans Serif

Colors
3276b5
faa54b
0355a3
fac994

Requirements
Must have
• Ideally would use Wordpress theme (Divi for example or other)
• Very smart front end
• Will upload logo soon
• (Harlow Net Learning)
• harlownetlearning.edu.au
• Graphics of 'people' pretty important - with a variety of ages.
Nice to have
• Interesting page
• National presence
• A bit University looking
• Professional
• Graphics of people
• Blog
• Graphics of people
• Age range from job seekers, to business folk, etc

```html
<!DOCTYPE html>
<html lang="en">
<head>
<meta charset="utf-8">
<title>Harlow Net Learning</title>
<link href="https://fonts.googleapis.com/css2?family=Raleway:wght@500;600;700&family=Open+Sans:wght@400;600;700&display=swap" rel="stylesheet">
<style>
:root{
  --orange:#f68b2c;
  --orange-light:#f9a552;
  --navy:#0b3b8e;
  --navy-deep:#08307a;
  --grey-card:#eeeff1;
  --grey-band:#f1f1f1;
  --text:#333;
  --muted:#666;
  --white:#fff;
}
*{margin:0;padding:0;box-sizing:border-box}
html,body{width:1200px;height:2917px;overflow:hidden}
body{font-family:"Open Sans",Arial,sans-serif;color:var(--text);background:var(--white);position:relative}
.abs{position:absolute}
h1,h2,h3,h4{font-family:"Raleway",Arial,sans-serif}

/* header */
.site-header{position:absolute;left:0;top:0;width:1200px;height:123px;background:var(--white);border-top:4px solid var(--orange);z-index:5}
.brand-disc{position:absolute;left:135px;top:-5px;width:186px;height:186px;border-radius:50%;background:var(--white);z-index:6;display:flex;flex-direction:column;align-items:center;justify-content:center;text-align:center}
.brand-name{font-family:"Raleway",Arial,sans-serif;font-weight:700;color:var(--navy);font-size:25px;line-height:1.05;margin-top:18px}
.brand-tag{font-size:11px;color:var(--orange);letter-spacing:1px;margin-top:6px;font-weight:600}
.freecall{position:absolute;right:160px;top:26px;font-weight:700;font-size:17px;color:var(--navy)}
.freecall span{color:var(--orange)}
.freecall svg{vertical-align:-2px;margin-right:5px}
.main-nav{position:absolute;left:350px;top:80px;display:flex;gap:0;font-size:13.5px}
.main-nav a{color:#222;text-decoration:none;margin-right:35px}
.main-nav a.current{color:var(--navy)}
.main-nav a:last-child{margin-right:0}

/* hero */
.hero{position:absolute;left:0;top:123px;width:1200px;height:509px;background:linear-gradient(100deg,#3a3f48 0%,#5b6270 40%,#8d939c 65%,#c9cbcd 100%)}
.hero-copy{position:absolute;left:161px;top:200px;width:330px;color:var(--white)}
.hero-copy h1{font-size:33px;line-height:1.1;font-weight:700;letter-spacing:.5px}
.hero-copy p{font-size:12.5px;line-height:1.45;margin-top:14px}
.btn{display:inline-block;background:var(--orange);color:var(--white);font-family:"Raleway",Arial,sans-serif;font-weight:700;font-size:13px;text-transform:uppercase;text-align:center;text-decoration:none}
.hero-copy .btn{width:146px;height:39px;line-height:39px;margin-top:18px}
.hero-dots{position:absolute;left:576px;top:466px;display:flex;gap:8px}
.hero-dots i{width:9px;height:9px;border-radius:50%;background:rgba(255,255,255,.6)}
.hero-dots i.on{background:var(--orange)}

/* why */
.section-title{position:absolute;left:0;width:1200px;text-align:center;font-family:"Raleway",Arial,sans-serif;font-weight:600;font-size:22px;color:#333;letter-spacing:.5px}
.why-card{position:absolute;top:716px;width:282px;height:276px;background:var(--grey-card);text-align:center}
.why-card .top{height:134px;display:flex;align-items:center;justify-content:center;position:relative}
.why-card .top::after{content:"";position:absolute;bottom:-9px;left:50%;margin-left:-9px;border-left:9px solid transparent;border-right:9px solid transparent;border-top:9px solid}
.why-card.orange .top{background:var(--orange)}
.why-card.orange .top::after{border-top-color:var(--orange)}
.why-card.navy .top{background:var(--navy)}
.why-card.navy .top::after{border-top-color:var(--navy)}
.ring{width:86px;height:86px;border:2px solid var(--white);border-radius:50%;display:flex;align-items:center;justify-content:center}
.why-card h3{font-size:18px;font-weight:600;margin-top:26px;color:#222}
.why-card p{font-size:11.5px;line-height:1.6;color:#555;padding:10px 28px 0}

/* welcome */
.welcome{position:absolute;left:0;top:1044px;width:1200px;height:397px;background:linear-gradient(90deg,#1d232b 0%,#2c333d 45%,#3f4853 75%,#56606a 100%)}
.welcome-copy{position:absolute;left:161px;top:78px;width:540px;color:var(--white)}
.welcome-copy h2{font-size:23px;line-height:1.25;font-weight:600;letter-spacing:.5px}
.welcome-copy p{font-size:11.5px;line-height:1.72;margin-top:20px;color:#e8e8e8}
.welcome-copy .btn{width:128px;height:39px;line-height:39px;margin-top:18px}
.device{position:absolute;left:792px;top:61px;width:264px;height:336px;border-radius:34px 34px 0 0;background:linear-gradient(180deg,#e9eaec 0%,#dcdde0 100%)}
.device .screen{position:absolute;left:16px;top:58px;right:16px;bottom:0;background:linear-gradient(180deg,#1a4aa0,#0b3b8e)}

/* courses */
.course{position:absolute;width:282px}
.course .photo{height:173px}
.course .label{height:56px;background:var(--grey-card);text-align:center;line-height:56px;font-family:"Raleway",Arial,sans-serif;font-weight:600;font-size:15px;color:#222;text-transform:uppercase;position:relative}
.course .label.pointer::before{content:"";position:absolute;top:0;left:50%;margin-left:-8px;border-left:8px solid transparent;border-right:8px solid transparent;border-top:8px solid #2c4f8c}
.view-more{position:absolute;left:538px;top:2046px;width:124px;height:40px;line-height:40px;background:var(--navy)}

/* testimonials */
.testimonials{position:absolute;left:0;top:2124px;width:1200px;height:280px;background:linear-gradient(180deg,var(--orange-light) 0%,var(--orange) 100%)}
.testimonials h2{position:absolute;top:50px;width:1200px;text-align:center;color:var(--white);font-size:23px;font-weight:600;letter-spacing:.5px}
.avatar{position:absolute;left:161px;top:104px;width:117px;height:117px;border-radius:50%;border:4px solid var(--white);background:linear-gradient(160deg,#c9ced6,#55627a)}
.avatar-badge{position:absolute;left:234px;top:184px;width:40px;height:40px;border-radius:50%;background:var(--navy);border:3px solid var(--white);display:flex;align-items:center;justify-content:center}
.quote{position:absolute;left:298px;top:112px;width:745px;color:var(--white);font-style:italic;font-size:11.3px;line-height:1.72}
.quote-by{position:absolute;left:298px;top:199px;color:var(--white);font-size:10px;font-weight:600}

/* customers */
.customers{position:absolute;left:0;top:2404px;width:1200px;height:208px;background:var(--grey-band)}
.logo-box{position:absolute;top:103px;width:165px;height:61px;background:var(--white);border:1px solid #d8d8d8;display:flex;align-items:center;justify-content:center;font-family:"Open Sans",Arial,sans-serif;font-weight:700;font-size:17px;color:var(--navy)}
.carousel-arrow{position:absolute;top:122px;font-size:18px;color:#666}

/* footer */
.site-footer{position:absolute;left:0;top:2612px;width:1200px;height:305px;background:var(--navy);color:var(--white)}
.footer-brand{position:absolute;left:161px;top:62px;width:164px;text-align:center}
.footer-brand .name{font-family:"Raleway",Arial,sans-serif;font-weight:700;font-size:25px;line-height:1.1}
.footer-brand .tag{font-size:11px;letter-spacing:1px;margin-top:8px}
.footer-col{position:absolute;top:48px}
.footer-col h4{font-size:16px;font-weight:700;letter-spacing:.5px;margin-bottom:14px}
.footer-col ul{list-style:none;font-size:9.5px;line-height:19px;text-transform:uppercase}
.footer-col p{font-size:11px;line-height:1.6;width:292px}
.email-field{width:290px;height:34px;background:var(--white);color:#333;font-size:11px;padding:0 10px;line-height:34px;margin-top:12px}
.subscribe{width:109px;height:35px;line-height:35px;margin-top:10px}
.footer-bar{position:absolute;left:0;top:251px;width:1200px;border-top:1px solid rgba(255,255,255,.25)}
.copyright{position:absolute;left:161px;top:272px;font-size:10px}
.socials{position:absolute;left:909px;top:266px;display:flex;gap:9px}
.socials span{width:28px;height:28px;border-radius:50%;border:1px solid var(--white)}
.page-code{position:absolute;left:1080px;top:274px;font-size:9px}
.chat-tab{position:absolute;left:1167px;top:2688px;width:33px;height:122px;background:var(--orange);color:var(--white);font-size:12px;font-weight:700;writing-mode:vertical-rl;transform:rotate(180deg);text-align:center;line-height:33px;z-index:8}
</style>
</head>
<body>

<header class="site-header">
  <div class="freecall"><svg width="14" height="14" viewBox="0 0 24 24"><rect width="24" height="24" rx="4" fill="#0b3b8e"/><path d="M8 5l2.5 3-1.5 2c1 2 2.5 3.5 4.5 4.5l2-1.5 3 2.5-1.5 2.5C11 18 6 13 5.5 6.5z" fill="#fff"/></svg>FREECALL: <span>1800 555 014</span></div>
  <nav class="main-nav">
    <a class="current">Home</a><a>About</a><a>Testimonials</a><a>Courses</a><a>For Employers</a><a>Support &amp; Resources</a><a>Blog</a><a>Contact Us</a>
  </nav>
</header>
<div class="brand-disc">
  <div class="brand-name">HARLOW NET<br>LEARNING</div>
  <div class="brand-tag">ONLINE TRAINING</div>
</div>

<section class="hero" role="img" aria-label="Photo of a woman working on a laptop at a café table">
  <div class="hero-copy">
    <h1>HARLOW NET<br>LEARNING</h1>
    <p>Sed ut perspiciatis unde omnis iste natuse sit voluptatem accusantium doloremque laudantium, totam rem aperia meaque ipsa quae ab illo.</p>
    <a class="btn">Apply Online</a>
  </div>
  <div class="hero-dots"><i></i><i class="on"></i><i></i><i></i></div>
</section>

<h2 class="section-title" style="top:664px">WHY HARLOW ONLINE</h2>

<div class="why-card orange" style="left:161px">
  <div class="top"><div class="ring"><svg width="30" height="30" viewBox="0 0 24 24" fill="#fff"><path d="M7 10V7a5 5 0 0110 0v3h-2V7a3 3 0 00-6 0v3z"/><rect x="5" y="10" width="14" height="11" rx="1.5"/></svg></div></div>
  <h3>FLEXIBLE</h3>
  <p>Sed ut perspiciatis unde omnis iste natusr sit voluptatem accusantium doloremque laudantium, totam rem aperiam, eaque ipsa quae ab illo</p>
</div>
<div class="why-card navy" style="left:459px">
  <div class="top"><div class="ring"><svg width="34" height="34" viewBox="0 0 24 24" fill="#fff"><path d="M21 3L3 11l6 2.5L21 3 10.5 14.5V21l3-4.5 4.5 2z"/></svg></div></div>
  <h3>VALUE</h3>
  <p>Sed ut perspiciatis unde omnis iste natusr sit voluptatem accusantium doloremque laudantium, totam rem aperiam, eaque ipsa quae ab illo</p>
</div>
<div class="why-card navy" style="left:757px">
  <div class="top"><div class="ring"><svg width="36" height="36" viewBox="0 0 24 24" fill="#fff"><circle cx="12" cy="8" r="3"/><circle cx="5.5" cy="9.5" r="2.2"/><circle cx="18.5" cy="9.5" r="2.2"/><path d="M6.5 19c0-4 2.5-6 5.5-6s5.5 2 5.5 6z"/><path d="M1.5 18c0-3 1.7-4.7 4-4.7 1 0 1.6.3 2 .6C6.3 15 5.6 16.4 5.5 18z"/><path d="M22.5 18c0-3-1.7-4.7-4-4.7-1 0-1.6.3-2 .6 1.2 1.1 1.9 2.5 2 4.1z"/></svg></div></div>
  <h3>EXPERIENCE</h3>
  <p>Sed ut perspiciatis unde omnis iste natusr sit voluptatem accusantium doloremque laudantium, totam rem aperiam, eaque ipsa quae ab illo</p>
</div>

<section class="welcome" role="img" aria-label="Dimmed photo of people working in an office">
  <div class="welcome-copy">
    <h2>WELCOME TO<br>HARLOW NET LEARNING</h2>
    <p>Harlow Net Learning is one of Australia's leading provider of flexible and affordable online continuing professional development programs, with over 600 online courses now available. Our range of self-paced online courses are delivered completely online via our e-learning system 24/7. We offer a range of popular online courses in accounting, finance, bookkeeping, management, marketing, information technology, project management and more. Our online courses are industry relevant and are designed to help you achieve your career goals. Harlow specialise in online Zentrosoft product training - prefect. Studying online allows you to balance study with your existing work and home life commitments.</p>
    <a class="btn">Read More</a>
  </div>
  <div class="device" role="img" aria-label="Smartphone showing the learning portal"><div class="screen"></div></div>
</section>

<h2 class="section-title" style="top:1467px">OUR COURSES</h2>

<div class="course" style="left:161px;top:1519px"><div class="photo" role="img" aria-label="Photo of a site worker in hard hat and safety vest" style="background:linear-gradient(135deg,#c9a27a,#e07a35 55%,#6d6f75)"></div><div class="label">Workplace Safety</div></div>
<div class="course" style="left:459px;top:1519px"><div class="photo" role="img" aria-label="Photo of a smiling saleswoman at a meeting" style="background:linear-gradient(135deg,#6c6460,#c9beb4 55%,#e9e6e1)"></div><div class="label">Sales Training</div></div>
<div class="course" style="left:757px;top:1519px"><div class="photo" role="img" aria-label="Photo of a team meeting in a bright boardroom" style="background:linear-gradient(135deg,#e7eaee,#b9c2cc 55%,#5b6675)"></div><div class="label">Leadership</div></div>
<div class="course" style="left:161px;top:1774px"><div class="photo" role="img" aria-label="Photo of colleagues discussing at a table" style="background:linear-gradient(135deg,#3b4656,#9aa4b1 50%,#d9dde1)"></div><div class="label">Process Management</div></div>
<div class="course" style="left:459px;top:1774px"><div class="photo" role="img" aria-label="Photo of hands reviewing charts on paper" style="background:linear-gradient(135deg,#dfe6ef,#a9bdd6 50%,#3e5f8e)"></div><div class="label pointer">Business Planning</div></div>
<div class="course" style="left:757px;top:1774px"><div class="photo" role="img" aria-label="Photo of a presenter addressing a seated group" style="background:linear-gradient(135deg,#d6d9dd,#8e949c 50%,#3a3f48)"></div><div class="label">Meetings and Events</div></div>

<a class="btn view-more">View More</a>

<section class="testimonials">
  <h2>CLIENT TESTIMONIALS</h2>
  <div class="avatar" role="img" aria-label="Portrait photo of a client"></div>
  <div class="avatar-badge"><svg width="18" height="18" viewBox="0 0 24 24" fill="#fff"><path d="M4 18v-6c0-4 2-6 6-7v3c-2 .5-3 1.5-3 4h3v6zM14 18v-6c0-4 2-6 6-7v3c-2 .5-3 1.5-3 4h3v6z"/></svg></div>
  <p class="quote">&ldquo; At vero eos et accusamus et iusto odio dignissimos ducimus qui blanditiis praesentium voluptatum deleniti atque corrupti quos dolores et quas mol estias excepturi sint occaecati cupiditate non provident, similique sunt in culpa qui officia deserunt mollitia animi, id est laborum et dolorum fuga. Et harum quidem rerum facilis est et expedita distinctio. Nam libero tempore, cum soluta nobis est eligendi optio cumque nihil impedit quo minus id quod maxime placeat facere uidere rerum facilis est et expedita distinctioam libero &rdquo;</p>
  <div class="quote-by">JHO SMITH, CITY NAME</div>
</section>

<section class="customers">
  <h2 class="section-title" style="top:53px">OUR CUSTOMERS</h2>
  <span class="carousel-arrow" style="left:128px">&#8249;</span>
  <div class="logo-box" style="left:161px">Brindle Foods</div>
  <div class="logo-box" style="left:339px">Coralbay</div>
  <div class="logo-box" style="left:517px">Swiftline</div>
  <div class="logo-box" style="left:695px">Vantel</div>
  <div class="logo-box" style="left:873px">Aerodyne Works</div>
  <span class="carousel-arrow" style="left:1058px">&#8250;</span>
</section>

<footer class="site-footer">
  <div class="footer-brand">
    <div class="name">HARLOW NET<br>LEARNING</div>
    <div class="tag">ONLINE TRAINING</div>
  </div>
  <div class="footer-col" style="left:383px">
    <h4>LINKS</h4>
    <ul><li>Home</li><li>About</li><li>Testimonials</li><li>Courses</li><li>For Employers</li><li>Support and Resources</li><li>Blog</li><li>Contact Us</li></ul>
  </div>
  <div class="footer-col" style="left:562px">
    <h4>COURSES</h4>
    <ul><li>Workplace Safety</li><li>Sales Training</li><li>Leadership</li><li>Process Management</li><li>Problem Solving</li><li>Project Management</li><li>Business Planning</li><li>View All</li></ul>
  </div>
  <div class="footer-col" style="left:747px">
    <h4>SUBSCRIBE TO NEWSLETTER</h4>
    <p>Sed ut perspiciatis unde omnis iste natus error sit voluptate mcc usantium doloremque laudantium, totam rem.</p>
    <div class="email-field">Email address</div>
    <a class="btn subscribe">Subscribe</a>
  </div>
  <div class="footer-bar"></div>
  <div class="copyright">&copy; 2016 All copyrights are reserved. Harlow Net Learning</div>
  <div class="socials" aria-label="Social links"><span></span><span></span><span></span><span></span></div>
  <div class="page-code">C4</div>
</footer>
<div class="chat-tab">ONLINE CHAT</div>

</body>
</html>
```